Nestlyo Business Card Project showing the logo and a vonka image on the rear

Design a whacky but professional business card, the logo is for the front and the Vonka image is for the rear. Happy to consider other open source Vonka Images if the designer wants to select one from the web. Nestlyo is a competitor to KPX.com.au and Plotfield.com.au and is based around every property in Australia

Business

Name, Title, Email, Web, Phone Number

• avenir

• Image on Back logo on front
• Happy to consider other images on rear, preftably Oscar Vonka. Image supplied I own, we can use open source other Vonka Images

```html
<!DOCTYPE html>
<html lang="en">
<head>
<meta charset="utf-8">
<title>Nestlyo Business Card</title>
<link href="https://fonts.googleapis.com/css2?family=Nunito+Sans:wght@400;800&display=swap" rel="stylesheet">
<style>
:root{
  --bg:#d9d9db;
  --orange:#f39220;
  --ink:#111111;
  --text:#333333;
  --white:#ffffff;
  --art-green:#3f6b2a;
  --art-olive:#6a5a1e;
  --art-orange:#e8641c;
  --art-red:#d8401a;
}
*{box-sizing:border-box;margin:0;padding:0}
html,body{width:1200px;height:900px;overflow:hidden}
body{background:var(--bg);font-family:"Nunito Sans",sans-serif;position:relative}
.card{position:absolute;width:600px;height:343px;border-radius:22px;overflow:hidden;box-shadow:0 10px 24px rgba(0,0,0,.25)}
.card-rear{left:110px;top:70px}
.rear-art{position:absolute;inset:0;background:
  linear-gradient(160deg,var(--art-green) 0%,var(--art-olive) 35%,var(--art-orange) 65%,var(--art-red) 85%,var(--art-olive) 100%)}
.rear-brand{position:absolute;right:60px;top:140px;display:flex;align-items:center;gap:14px;color:var(--white);font-weight:800;font-size:54px;letter-spacing:1px}
.brand-square{width:34px;height:34px;background:var(--orange);display:inline-block;flex:none}
.card-front{left:490px;top:480px;background:var(--white)}
.front-brand{position:absolute;left:48px;top:52px;display:flex;align-items:center;gap:14px;color:var(--ink);font-weight:800;font-size:46px}
.front-brand .brand-square{width:30px;height:30px}
.person{position:absolute;left:56px;right:30px;top:150px}
.name-row{display:flex;align-items:center;gap:12px}
.person-name{color:var(--orange);font-weight:800;font-size:24px;letter-spacing:1px;text-transform:uppercase;white-space:nowrap}
.rule{flex:1;height:1px;background:var(--ink);margin-top:6px}
.person-title{color:var(--text);font-size:17px;margin-top:2px}
.contacts{position:absolute;left:56px;top:224px;list-style:none}
.contacts li{display:flex;align-items:center;gap:8px;color:var(--text);font-size:16px;line-height:24px;white-space:nowrap}
.contacts svg{width:16px;height:16px;flex:none}
.address{position:absolute;right:34px;top:230px;text-align:right;color:var(--text);font-size:15px;line-height:20px;white-space:nowrap}
.band{position:absolute;left:0;right:0;bottom:0;height:14px;background:var(--orange)}
</style>
</head>
<body>
  <section class="card card-rear">
    <div class="rear-art" role="img" aria-label="Colourful whimsical cityscape illustration of playful buildings, clouds, stars and a sun in green, orange and red tones"></div>
    <div class="rear-brand"><span class="brand-square"></span>Nestlyo</div>
  </section>

  <section class="card card-front">
    <div class="front-brand"><span class="brand-square"></span>Nestlyo</div>
    <div class="person">
      <div class="name-row">
        <p class="person-name">Daniel Carrow</p>
        <span class="rule"></span>
      </div>
      <p class="person-title">Executive Producer</p>
    </div>
    <ul class="contacts">
      <li><svg viewBox="0 0 16 16"><circle cx="8" cy="8" r="8" fill="#f39220"/><path d="M5 4.5l1.5-.5 1 2-1 .8a5 5 0 0 0 2.7 2.7l.8-1 2 1-.5 1.5c-3 .3-6.8-3.5-6.5-6.5z" fill="#fff"/></svg>323-555-0148</li>
      <li><svg viewBox="0 0 16 16"><circle cx="8" cy="8" r="8" fill="#f39220"/><rect x="4" y="5.5" width="8" height="5.5" fill="#fff"/><path d="M4 5.5l4 3 4-3" fill="none" stroke="#f39220" stroke-width="0.8"/></svg>Daniel@nestlyo.com.au</li>
      <li><svg viewBox="0 0 16 16"><circle cx="8" cy="8" r="8" fill="#f39220"/><circle cx="8" cy="8" r="4" fill="none" stroke="#fff" stroke-width="1.2"/><path d="M4 8h8M8 4c-2 2.5-2 5.5 0 8M8 4c2 2.5 2 5.5 0 8" fill="none" stroke="#fff" stroke-width="0.8"/></svg>www.nestlyo.com.au</li>
    </ul>
    <div class="address">
      <p>1480 W Harlow Street</p>
      <p>Corrin Shire 4417</p>
    </div>
    <div class="band"></div>
  </section>
</body>
</html>
```